New modern business card design

To design a brand new business card that's clean & modern in terms of layout.
I have attached our company logo and also basic information regarding what is needed on the card that also needs to be editable.

Target Market(s)

motor trade

Contact Information for Business Card

logo, name, title, tel, mob, email, address, www, all information is in the word.doc file

Requirements
Must have
• white background
Nice to have
• Nice clean font

```html
<!DOCTYPE html>
<html lang="en">
<head>
<meta charset="utf-8">
<title>Bolt Forge Ltd – Business Card Options</title>
<link rel="stylesheet" href="https://fonts.googleapis.com/css2?family=Arimo:wght@400;700&display=swap">
<style>
  :root {
    --board: #d1d2d4;
    --card: #ffffff;
    --brand-blue: #1375bc;
    --text-grey: #6d6e71;
    --muted-grey: #8a8b8e;
    --divider: #5b86d6;
  }
  * { margin: 0; padding: 0; box-sizing: border-box; }
  html, body { width: 1200px; height: 1200px; overflow: hidden; }
  body {
    background: var(--board);
    font-family: "Arimo", Arial, sans-serif;
    color: var(--text-grey);
    position: relative;
  }
  .card {
    position: absolute;
    left: 245px;
    width: 711px;
    height: 406px;
    background: var(--card);
    box-shadow: 0 2px 8px rgba(0,0,0,0.18);
    overflow: hidden;
  }
  .card--one { top: 134px; }
  .card--two { top: 660px; }
  .card__band {
    position: absolute; left: 0; right: 0; bottom: 0;
    height: 32px; background: var(--brand-blue);
  }
  .option-label {
    position: absolute; left: 0; width: 1200px;
    text-align: center; font-size: 19px; color: var(--text-grey);
  }
  .option-label--one { top: 561px; }
  .option-label--two { top: 1088px; }

  /* wordmark */
  .wordmark {
    position: absolute;
    display: flex; flex-direction: column; align-items: center;
    width: 280px;
  }
  .wordmark__square {
    width: 52px; height: 52px; background: var(--brand-blue); margin-bottom: 16px;
  }
  .wordmark__name {
    font-weight: 700; font-size: 29px; letter-spacing: 1px;
    color: var(--brand-blue); white-space: nowrap;
  }
  .wordmark__rule {
    width: 100%; height: 1.5px; background: var(--brand-blue); margin-top: 10px;
  }
  .card--one .wordmark { left: 40px; top: 128px; }
  .card--two .wordmark { left: 36px; top: 40px; }

  /* option one */
  .divider {
    position: absolute; left: 355px; top: 37px; width: 2px; height: 320px;
    background: linear-gradient(to bottom, rgba(91,134,214,0), var(--divider) 30%, var(--divider) 70%, rgba(91,134,214,0));
  }
  .person__name { font-weight: 700; font-size: 28px; color: var(--brand-blue); line-height: 1.1; }
  .person__title { font-size: 18px; color: var(--muted-grey); line-height: 1.3; }
  .person__mobile { font-size: 27px; line-height: 1.3; }
  .details { font-size: 18px; line-height: 24px; }
  .card--one .person { position: absolute; left: 392px; top: 70px; }
  .card--one .person__mobile { margin-top: 4px; }
  .card--one .details--email { position: absolute; left: 392px; top: 153px; }
  .card--one .details--address { position: absolute; left: 392px; top: 212px; }
  .card--one .details--web { position: absolute; left: 392px; top: 287px; }

  /* option two */
  .card--two .person { position: absolute; right: 40px; top: 150px; text-align: right; }
  .card--two .person__title { margin-top: 2px; }
  .card--two .person__mobile { margin-top: 4px; }
  .card--two .details--address {
    position: absolute; left: 41px; top: 288px; line-height: 26px;
  }
  .contact-list {
    position: absolute; left: 381px; top: 288px; list-style: none;
    font-size: 18px; line-height: 26px;
  }
  .contact-list li { display: flex; align-items: center; gap: 9px; }
  .contact-list svg { width: 19px; height: 19px; flex: none; }
</style>
</head>
<body>

  <section class="card card--one">
    <div class="wordmark">
      <div class="wordmark__square"></div>
      <div class="wordmark__name">BOLT FORGE LTD</div>
      <div class="wordmark__rule"></div>
    </div>
    <div class="divider"></div>
    <div class="person">
      <div class="person__name">Daniel Harper</div>
      <div class="person__title">General Manager</div>
      <div class="person__mobile">07700 900 418</div>
    </div>
    <div class="details details--email">dharper@boltforge.co.uk</div>
    <div class="details details--address">Kestrel Road<br>Ashworth, Northfield<br>NF4 2QT</div>
    <div class="details details--web">Tel: 0161 496 0812<br>www.boltforge.co.uk</div>
    <div class="card__band"></div>
  </section>
  <div class="option-label option-label--one">option 1</div>

  <section class="card card--two">
    <div class="wordmark">
      <div class="wordmark__square"></div>
      <div class="wordmark__name">BOLT FORGE LTD</div>
      <div class="wordmark__rule"></div>
    </div>
    <div class="person">
      <div class="person__name">Daniel Harper</div>
      <div class="person__title">General Manager</div>
      <div class="person__mobile">07700 900 418</div>
    </div>
    <div class="details details--address">Kestrel Road<br>Ashworth, Northfield<br>NF4 2QT</div>
    <ul class="contact-list">
      <li>
        <svg viewBox="0 0 20 20" aria-hidden="true"><circle cx="10" cy="10" r="10" fill="#1375bc"/><rect x="5" y="6.5" width="10" height="7" fill="none" stroke="#fff" stroke-width="1.3"/><path d="M5 6.5 L10 10.8 L15 6.5" fill="none" stroke="#fff" stroke-width="1.3"/></svg>
        dharper@boltforge.co.uk
      </li>
      <li>
        <svg viewBox="0 0 20 20" aria-hidden="true"><circle cx="10" cy="10" r="10" fill="#1375bc"/><path d="M7 5 L9 7.5 L8 9 Q9.5 11.5 11 12 L12.5 11 L15 13 L13.5 15 Q8 14.5 5.5 7 Z" fill="#fff"/></svg>
        0161 496 0812
      </li>
      <li>
        <svg viewBox="0 0 20 20" aria-hidden="true"><circle cx="10" cy="10" r="10" fill="#1375bc"/><g fill="none" stroke="#fff" stroke-width="1.1"><circle cx="10" cy="10" r="5.5"/><ellipse cx="10" cy="10" rx="2.4" ry="5.5"/><path d="M4.5 10 H15.5 M5.3 7.3 H14.7 M5.3 12.7 H14.7"/></g></svg>
        www.boltforge.co.uk
      </li>
    </ul>
    <div class="card__band"></div>
  </section>
  <div class="option-label option-label--two">option 2</div>

</body>
</html>
```